RM Tomás Rivera (Business Card)

Hi designers, in this work, I'm looking for an sophisticated stylish, elegant and proffesional personal card. We have a laboratory of pathology automated, with equipments high quality.
In this web the designers, have created my business logo, the name is "RM Tomás Rivera"
In our lab, we principal work is to prepare the biopsies for further diagnostic of diseases like cancer, tumors, etc.
I need that the first face, only having my complete logo (Rm Tomás Rivera, Laboratorio de procesamiento Histologico)
The overleaf, could repeat the same logo, like water logo.
In this face, I need to say: My full data:

Técnico en Anatomía Patológica
Tomás Rivera Ibarra M.P 47203
Av. Paredes Luján 418 - 2do piso - Instituto Marbel.
Córdoba, Argentina
(0351) 154820937
rivera.tomas@correolab.example

with respect the colors of card, use your imagination, the original logo color is violet, I haven't chosen a color base for the card.

attached pictures are examples of cards I like your DESIGN.
Attached too, the original logo to my company.

the size of card are:
horizontal: 9cm
vertical: 5,5cm

any question that you have, not doubt to question me,
Hand to work!

Industry/Entity Type

Laboratory

Requirements
Must have
• designers sophisticated, not simples, like show the images attached

```html
<!DOCTYPE html>
<html lang="es">
<head>
<meta charset="utf-8">
<title>Tomás Rivera — Tarjeta personal</title>
<link rel="stylesheet" href="https://fonts.googleapis.com/css2?family=PT+Sans&family=Roboto+Condensed:wght@400&display=swap">
<style>
  :root {
    --backdrop: #6d6e70;
    --card: #ffffff;
    --violet: #622181;
    --grey: #8a8a8c;
    --grey-dark: #77787b;
    --on-violet: #ffffff;
  }
  * { margin: 0; padding: 0; box-sizing: border-box; }
  html, body {
    width: 1200px; height: 458px; overflow: hidden;
    background: var(--backdrop);
  }
  .canvas { position: relative; width: 1200px; height: 458px; }
  .card {
    position: absolute; top: 75px;
    width: 516px; height: 298px;
    background: var(--card); overflow: hidden;
  }
  .card--front { left: 48px; }
  .card--back { left: 601px; }
  .card__wave { position: absolute; inset: 0; }
  .wave__band { fill: var(--violet); }
  .wave__rule { fill: none; stroke: var(--grey); stroke-width: 5; }

  .brand-name {
    position: absolute; left: 0; right: 0; text-align: center;
    font-family: "PT Sans", sans-serif; font-weight: 400;
    color: var(--grey-dark); letter-spacing: 6px; text-transform: uppercase;
  }
  .card--front .brand-name { top: 58px; font-size: 34px; }
  .card--back .brand-name { top: 62px; font-size: 36px; }

  .brand-rule {
    position: absolute; left: 107px; top: 117px;
    width: 306px; height: 4px; background: var(--grey);
  }
  .brand-tagline {
    position: absolute; left: 0; right: 0; top: 125px; text-align: center;
    font-family: "Roboto Condensed", sans-serif; font-size: 22px;
    color: var(--grey-dark); letter-spacing: -0.2px;
  }

  .holder {
    position: absolute; left: 0; right: 0; top: 202px; text-align: center;
    font-family: "PT Sans", sans-serif; font-size: 13px;
    color: var(--on-violet); letter-spacing: 4.5px; text-transform: uppercase;
  }
  .contact, .address {
    position: absolute; font-family: "PT Sans", sans-serif;
    font-size: 13.5px; line-height: 17px; color: var(--on-violet);
  }
  .contact { left: 20px; top: 252px; }
  .address { right: 24px; top: 227px; text-align: right; }

  .band-tagline {
    position: absolute; left: 0; right: 0; top: 246px; text-align: center;
    font-family: "Roboto Condensed", sans-serif; font-size: 22px;
    color: var(--on-violet);
  }
</style>
</head>
<body>
<main class="canvas">

  <section class="card card--front" aria-label="Frente de la tarjeta">
    <svg class="card__wave" width="516" height="298" viewBox="0 0 516 298" aria-hidden="true">
      <path class="wave__band" d="M0,252 C110,196 390,178 516,229 L516,298 L0,298 Z"/>
      <path class="wave__rule" d="M0,243 C110,186 390,168 516,220"/>
    </svg>
    <p class="brand-name">Tomás Rivera</p>
    <div class="brand-rule"></div>
    <p class="brand-tagline">LABORATORIO DE PROCESAMIENTO HISTOLOGICO</p>

    <p class="holder">Tomás Rivera</p>
    <p class="contact">(0351) 154820937<br>rivera.tomas@correolab.example</p>
    <p class="address">Tomás Rivera Ibarra M.P 47203<br>Av. Paredes Luján 418<br>2do piso-Instituto Marbel.<br>Córdoba, Argentina</p>
  </section>

  <section class="card card--back" aria-label="Dorso de la tarjeta">
    <svg class="card__wave" width="516" height="298" viewBox="0 0 516 298" aria-hidden="true">
      <path class="wave__band" d="M0,252 C110,196 390,178 516,229 L516,298 L0,298 Z"/>
      <path class="wave__rule" d="M0,243 C110,186 390,168 516,220"/>
    </svg>
    <p class="brand-name">Tomás Rivera</p>
    <p class="band-tagline">LABORATORIO DE PROCESAMIENTO HISTOLOGICO</p>
  </section>

</main>
</body>
</html>
```